Business card for a Exhibition booth fabrication company

Hi. My company would like to change our corporate name card. We are an events and Exhibition stand builder company. We would like our corporate name card to resonate what we do. I need someone to create something unique that relates to the industry that I am in. The graphic designer should be creative to incorporate the elements of my industry and try to blend in well in the design of the card. Our aim is to ensure that we are unique and our card can look different from our competitors.
Updates

The decision maker was very busy and didnt had time to make this decision

Target Market(s)

Marketing and events manager from all companies

Contact Information for Business Card

The business card should have the following details:
Name
Job Title
Email
Website

Colors

Designer to choose colors to be used in the design.

Requirements
Must have
• The card must be look something that is relevant to the service that I am providing. My website is: www.velmora-buildworks.example
• You can see my website to get more information on what service that I am doing
Nice to have
• On the back of my card, I would like to have a globe image with the incorporation of my company logo. This is to indicate that my services can be done in any part of the world.

```html
<!DOCTYPE html>
<html lang="en">
<head>
<meta charset="utf-8">
<title>Velmora Buildworks – Business Card</title>
<link rel="stylesheet" href="https://fonts.googleapis.com/css2?family=Montserrat:wght@600;700&family=Open+Sans:wght@400;600&display=swap">
<style>
  :root {
    --bg: #e9e6e1;
    --slate: #5f6062;
    --slate-light: #7a7b7d;
    --red: #e31b23;
    --white: #ffffff;
    --ink: #4a4b4d;
  }
  * { box-sizing: border-box; margin: 0; padding: 0; }
  html, body { width: 1200px; height: 900px; overflow: hidden; }
  body { background: var(--bg); font-family: "Open Sans", sans-serif; position: relative; }

  .card {
    position: absolute;
    width: 600px;
    height: 343px;
    border-radius: 4px;
    overflow: hidden;
    box-shadow: 0 6px 18px rgba(0,0,0,0.18);
  }

  /* Back side */
  .card-back { left: 60px; top: 70px; background: var(--slate); color: var(--white); }
  .world-map {
    position: absolute; left: 40px; top: 25px; width: 520px; height: 290px;
    background: radial-gradient(ellipse at center, rgba(255,255,255,0.22), rgba(255,255,255,0.06) 70%, rgba(255,255,255,0) 100%);
    border-radius: 40% 45% 40% 50%;
  }
  .back-content { position: absolute; inset: 0; text-align: center; padding-top: 92px; }
  .back-company {
    font-family: "Montserrat", sans-serif; font-weight: 700; font-size: 26px;
    letter-spacing: 3px; margin-bottom: 26px;
  }
  .services { list-style: none; font-size: 15px; line-height: 25px; }
  .sep {
    display: inline-block; width: 8px; height: 8px; border-radius: 50%;
    background: var(--red); margin: 0 8px; vertical-align: middle;
  }

  /* Front side */
  .card-front { left: 540px; top: 480px; background: var(--white); }
  .swoosh { position: absolute; inset: 0; }
  .person { position: absolute; left: 50px; top: 78px; }
  .person-name {
    font-family: "Montserrat", sans-serif; font-weight: 700; font-size: 24px;
    color: var(--red); letter-spacing: 0.5px; line-height: 1;
  }
  .person-title { font-size: 14px; color: var(--ink); margin-top: 4px; }
  .brand {
    position: absolute; right: 30px; top: 34px;
    display: flex; flex-direction: column; align-items: center; gap: 10px;
  }
  .brand-dot { width: 40px; height: 40px; border-radius: 50%; background: var(--red); }
  .brand-name {
    font-family: "Montserrat", sans-serif; font-weight: 700; font-size: 17px;
    letter-spacing: 2px; color: var(--slate);
  }
  .contacts { position: absolute; left: 50px; top: 140px; list-style: none; font-size: 14px; color: var(--ink); line-height: 24px; }
  .contacts li { display: flex; align-items: center; gap: 8px; }
  .contacts svg { width: 14px; height: 14px; fill: var(--red); flex: none; }
  .website {
    position: absolute; right: 24px; bottom: 40px;
    font-size: 14px; color: var(--white);
  }
</style>
</head>
<body>

<section class="card card-back" aria-label="Card back">
  <div class="world-map" role="img" aria-label="Dotted world map in light grey"></div>
  <div class="back-content">
    <h1 class="back-company">VELMORA BUILDWORKS</h1>
    <ul class="services">
      <li>Exhibition Booth Fabrication<span class="sep"></span>Outdoor Booth Setup</li>
      <li>Interior Design<span class="sep"></span>Installation and Dismantle</li>
      <li>Exhibition Management<span class="sep"></span>Shell Scheme Display Booth</li>
      <li>Custom Stand Design<span class="sep"></span>Exhibition Furniture and Equipment</li>
      <li>Exhibition Project Management</li>
    </ul>
  </div>
</section>

<section class="card card-front" aria-label="Card front">
  <svg class="swoosh" viewBox="0 0 600 343" preserveAspectRatio="none" aria-hidden="true">
    <path d="M0,334 C200,326 400,246 600,170 L600,343 L0,343 Z" fill="#5f6062"/>
    <path d="M0,300 C200,296 420,220 545,170 C400,240 220,318 0,322 Z" fill="#e31b23"/>
  </svg>

  <div class="person">
    <h2 class="person-name">DANIEL HARLOW</h2>
    <p class="person-title">Managing Director</p>
  </div>

  <div class="brand">
    <span class="brand-dot"></span>
    <span class="brand-name">VELMORA BUILDWORKS</span>
  </div>

  <ul class="contacts">
    <li><svg viewBox="0 0 16 16"><path d="M2 6c0-2 2-3 6-3s6 1 6 3v1h-3V5.5H5V7H2Z M4 8h8l2 5H2Z"/></svg>+65 84417209 (Singapore)</li>
    <li><svg viewBox="0 0 16 16"><path d="M2 6c0-2 2-3 6-3s6 1 6 3v1h-3V5.5H5V7H2Z M4 8h8l2 5H2Z"/></svg>+974 55128836 (Qatar)</li>
    <li><svg viewBox="0 0 16 16"><path d="M1 3h14v10H1Z M1 3l7 6 7-6" stroke="#fff" stroke-width="1"/></svg>info@velmora-buildworks.example</li>
  </ul>

  <p class="website">www.velmora-buildworks.example</p>
</section>

</body>
</html>
```